WORD Template for Training Manual called Lantern Road

I have written a training manual called Lantern Road. I need a design for the manual I can put the materials into for small groups of people to use.
This means a cover along with a page design that looks appealing but doesn't distract from the content.
We already have an organisational logo and colour scheme. It would be great to have at nine different page designs as the manual will have nine sessions of learning. So one design for each session of content.
I have uploaded some of the example materials we have designed from another designer as well so you can see the kind of look and feel our other materials have.
I have also uploaded the introduction and the first session of the content so you can use it to help shape the design.
As you will see in the sessions, each session has small group activities, discussion questions and a video content session for the group to watch. All nine sessions will be designed in a similar way.
There will also be a second booklet to design of daily reflections so a successful design for this workbook will lead to a second project with the same look and feel.
Updates
Need extra days to review
Target Market(s)
My target market is adults from 18-45
Industry/Entity Type
Christian Ministry
Look and feel
Each slider illustrates characteristics of the customer's brand and the style your logo design should communicate.

```html
<!DOCTYPE html>
<html lang="en">
<head>
<meta charset="utf-8">
<title>Lantern Road – Manual Pages</title>
<link rel="stylesheet" href="https://fonts.googleapis.com/css2?family=Open+Sans:wght@300;400;600;700;800&display=swap">
<style>
  :root {
    --backdrop: #9d9d9f;
    --paper: #ffffff;
    --lime: #bcdb5d;
    --purple: #674097;
    --purple-deep: #633c96;
    --purple-soft: #f2eff8;
    --ink: #333333;
    --heading-ink: #2b2b2b;
  }
  * { box-sizing: border-box; margin: 0; padding: 0; }
  html, body { width: 1200px; height: 2252px; overflow: hidden; }
  body {
    background: var(--backdrop);
    font-family: "Open Sans", Arial, sans-serif;
    color: var(--ink);
    position: relative;
  }
  .page {
    position: absolute;
    left: 136px;
    width: 927px;
    height: 656px;
    background: var(--paper);
    overflow: hidden;
  }
  .page--intro { top: 111px; }
  .page--divider { top: 798px; }
  .page--session { top: 1485px; }

  .edge { position: absolute; top: 0; width: 41px; height: 100%; }
  .edge--left { left: 0; }
  .edge--right { right: 0; }
  .page--intro .edge { background: var(--lime); }
  .page--session .edge { background: var(--purple); }

  .column {
    position: absolute;
    width: 388px;
    font-size: 12.6px;
    line-height: 19.2px;
  }
  .column p { margin-bottom: 16px; }
  .column--left { left: 62px; }
  .column--right { left: 479px; }

  .intro-title {
    font-size: 20.5px;
    font-weight: 600;
    color: var(--heading-ink);
    margin-bottom: 11px;
  }
  .folio {
    position: absolute;
    left: 0; right: 0;
    text-align: center;
    font-size: 11px;
    font-weight: 700;
    color: var(--purple);
  }

  /* divider page */
  .divider-field {
    position: absolute;
    left: 0; top: 0;
    width: 756px; height: 100%;
    background:
      radial-gradient(ellipse 420px 560px at 500px 260px, #6c4a9c 0%, rgba(108,74,156,0) 70%),
      radial-gradient(ellipse 300px 420px at 120px 520px, #6d4b9e 0%, rgba(109,75,158,0) 70%),
      var(--purple-deep);
  }
  .session-number {
    position: absolute;
    left: 862px; top: 42px;
    width: 30px;
    font-size: 38px;
    font-weight: 800;
    color: var(--purple);
    text-align: center;
  }
  .week-label {
    position: absolute;
    left: 472px; top: 271px;
    width: 284px; height: 65px;
    background: var(--paper);
    color: var(--purple);
    font-weight: 800;
    font-size: 40px;
    letter-spacing: 0.5px;
    display: flex; align-items: center; justify-content: flex-end;
    padding-right: 27px;
  }
  .session-arrow { position: absolute; left: 874px; top: 286px; }
  .session-title {
    position: absolute;
    right: 200px; top: 346px;
    text-align: right;
    color: var(--paper);
    font-weight: 300;
    font-size: 78px;
    line-height: 68px;
  }

  /* session page */
  .session-wash {
    position: absolute;
    left: 430px; top: 40px;
    width: 456px; height: 616px;
    background: radial-gradient(ellipse 300px 320px at 260px 330px, var(--purple-soft) 0%, rgba(242,239,248,0.6) 55%, rgba(255,255,255,0) 80%);
  }
  .label {
    color: var(--purple);
    font-weight: 700;
    font-size: 12.6px;
    margin-bottom: 7px;
  }
  .block { margin-bottom: 30px; }
  .block p { margin-bottom: 0; }
  .numbered { list-style: none; }
  .numbered > li {
    position: relative;
    padding-left: 26px;
    margin-bottom: 7px;
  }
  .numbered > li > .num { position: absolute; left: 0; top: 0; }
  .numbered--wide > li { padding-left: 31px; }
  .bullets { list-style: none; margin-top: 7px; }
  .bullets li { position: relative; padding-left: 19px; margin-bottom: 7px; }
  .bullets li::before {
    content: ""; position: absolute; left: 2px; top: 7px;
    width: 5px; height: 5px; border-radius: 50%; background: var(--ink);
  }
  .bullets--nested li { padding-left: 20px; }
  .bullets--nested { margin-left: -2px; }
</style>
</head>
<body>

  <section class="page page--intro">
    <div class="edge edge--left"></div>
    <div class="edge edge--right"></div>

    <div class="column column--left" style="top:60px">
      <h2 class="intro-title">Introduction</h2>
      <p>When I was a young boy, I loved games and adventures. Games I played with Mum and Dad, and the adventures I read in books or created in my imagination and played out in the backyard. One of my favourite games was pretty simple. I would start at the end of the hallway in our house, Mum would call me, and I would run down the hallway as fast as I could. When I got to the end of the hallway, I would leap into the air through the doorway into the kitchen, and she would catch me and give me a great big hug.</p>
      <p>One day I put my fertile imagination and this game together and decided to play the game with Dad. Dad came home from work one afternoon through the front door and headed down the hallway to the kitchen. He stood in the kitchen in clear view and was chatting with Mum. I imagined what it would be like to play this game with Dad; in my head, it all played out beautifully.</p>
      <p>So, I yelled out, “Dad, Dad, “and took off down the hallway as fast as my legs could carry me. Dad had a look in my direction and then looked back to Mum. I kept running down the hallway, and Dad looked back at me and waited for me to arrive; I got to the Kitchen doorway and leapt as high and as far as I had ever jumped in my life…</p>
      <p>I regained consciousness with blood running down my face and my dad saying, “I didn't know the game”. Mum was trying to stop the</p>
    </div>

    <div class="column column--right" style="top:98px">
      <p>bleeding, and my brain was struggling to figure out what had happened. It seems I had flown across the kitchen headfirst into the cupboards, cutting my head open on the cupboard door handle, a scar I retain to this day.</p>
      <p>For me, following Jesus can be a little like this, I think I have it figured out, and I embark on what I think God wants me to do; I hit my head and then wonder what on earth happened. At that point, wounded and bruised, God always brings me back to the basics. He calls me back to his simple commands to love others the way he loves me, to announce that He is here, that He loves others too, and to gather with other followers for worship, encouragement and support so we can follow Jesus together.</p>
      <p>Lantern Road takes followers of Jesus through those basic commands and their implications for our everyday life. My goal in developing this material is to teach you how to look at the world around you through Jesus' eyes, to see people the way He sees them, and then to pursue His mission as a part of your everyday being and doing. To move beyond believing in God and accepting his Grace and Forgiveness to living his commands faithfully and, by doing so, being part of God's transformation project, just like He always intended.</p>
    </div>

    <div class="folio" style="top:622px">4</div>
  </section>

  <section class="page page--divider">
    <div class="divider-field" role="img" aria-label="Deep purple field with large faint leaf shapes"></div>
    <div class="session-number">1</div>
    <div class="week-label">WEEK ONE</div>
    <svg class="session-arrow" width="20" height="38" viewBox="0 0 20 38" aria-hidden="true">
      <path d="M1 1 L19 19 L1 37 Z" fill="var(--purple)" stroke="#3d2363" stroke-width="1"/>
    </svg>
    <h1 class="session-title">What is<br>Love?</h1>
  </section>

  <section class="page page--session">
    <div class="edge edge--left"></div>
    <div class="edge edge--right"></div>
    <div class="session-wash" role="img" aria-label="Faint pale lilac leaf shapes"></div>

    <div class="column column--left" style="top:67px">
      <div class="block">
        <h3 class="label">Topic:</h3>
        <p>Love is a choice, followed by an action to step into the world of another and act self-sacrificially in that person's best interests.</p>
      </div>
      <div class="block">
        <h3 class="label">In this session, participants will learn to:</h3>
        <ol class="numbered">
          <li><span class="num">1)</span>Explain the biblical concept of Love as expressed by God through Jesus Christ</li>
          <li><span class="num">2)</span>Describe how they can express love towards others in their context.</li>
        </ol>
      </div>
      <div class="block">
        <h3 class="label">Resources you will need:</h3>
        <p>A3 Paper for drawing and Coloured Pencils/Textas for drawing.</p>
      </div>
      <div class="block">
        <h3 class="label">Pre-video activity</h3>
        <p>In groups of 3, draw a picture representing the moment the father welcomes his prodigal son home (Luke 15:11-32). Think about what it was the father was saying through his actions. What was the son saying through his actions? What was being expressed between them? This is not a picture of the moment like a photograph, but rather a picture representing it in a way that might not even have the father and son in it.</p>
      </div>
    </div>

    <div class="column column--right" style="top:67px">
      <div class="block" style="margin-bottom:18px">
        <h3 class="label">Show Video Content for What is Love?</h3>
      </div>
      <div class="block">
        <h3 class="label">Large Group Discussion</h3>
        <ul class="bullets">
          <li>Was there any content in the video that was new to you or expressed in a way that you hadn't heard before?</li>
          <li>What were the key points being made in the video?</li>
        </ul>
      </div>
      <div class="block">
        <h3 class="label">Small Group Discussion</h3>
        <p style="margin-bottom:7px">In groups of three, discuss the following questions.</p>
        <ol class="numbered numbered--wide">
          <li><span class="num">1)</span>When Jesus was born, God entered our world. God incarnate, God in human flesh. This is the moment God's revolution began when God chose to come and dwell amongst us. This is the heart of God's mission, to go and live with His created humans.
            <ul class="bullets bullets--nested">
              <li>What does it mean to you that God wants to live in your world and understand what life is like for you?</li>
            </ul>
          </li>
          <li><span class="num">2)</span>In doing this, God has expressed His love for each and every person He has created. Paul expressed this best in Romans 5:6-8, writing, “You see, just at the right time, when we were still powerless, Christ died for the ungodly. Very rarely will anyone die for a righteous person, though for a good person, someone might possibly dare to die. But God demonstrates his own love for us in this: While we were still sinners, Christ died for us.”</li>
        </ol>
      </div>
    </div>

    <div class="folio" style="top:638px">4</div>
  </section>

</body>
</html>
```